Business Card Design Project

Looking for a logo and business card for a Real State Business i will be opening. The name is not choosen yet , but will probably be RTV IMOVEIS.
I was thinking black and silver colors, but am open to nice ideas.
I did add a business card that i liked a lot, am looking for something like that, with logo in black or silver in a black card. The logo i was thinking in the letters RTV as i uploaded or something or little and cute buildings or a house...just ideas, can be any nice logo.
Updates

You guys can add other colors if you want, I like colors very "BRIGHT" and "open", like red, pink, strong colors. almost glow in the dark colors. lol

Designers,

I've increased more 88 dollars in the budget for 1st place cause I will want envelope designs... small and big sizes.

So 1st place is now U$248,00. 

No need to send the envelope designs right now... only the business cards designs.

Thank you.

Industry/Entity Type

Business

Requirements
Must have
• Renata Tavares Vilela

www.RTVimoveis-exemplo.com.br

+554188316402

renata@rtvimoveis-exemplo.com.br

```html
<!DOCTYPE html>
<html lang="pt-BR">
<head>
<meta charset="utf-8">
<title>RTV Imoveis – Cartão de Visita</title>
<link href="https://fonts.googleapis.com/css2?family=Michroma&display=swap" rel="stylesheet">
<style>
  :root {
    --backdrop: #3a322e;
    --card: #121212;
    --card-edge: #1c1c1c;
    --silver: #d6d6d6;
    --silver-soft: #a9a9a9;
    --gloss: #2a2a2a;
  }
  * { box-sizing: border-box; margin: 0; padding: 0; }
  html, body {
    width: 1200px; height: 716px; overflow: hidden;
    background: var(--backdrop);
    font-family: "Michroma", "Arial", sans-serif;
  }
  .stage {
    width: 1200px; height: 716px;
    display: flex; align-items: center; justify-content: center; gap: 48px;
  }
  .card {
    width: 520px; height: 300px;
    background: var(--card);
    border: 1px solid var(--card-edge);
    border-radius: 3px;
    position: relative;
    box-shadow: 0 14px 30px rgba(0,0,0,.45);
  }
  /* Front */
  .card--front {
    display: flex; align-items: center; justify-content: center; gap: 16px;
  }
  .brand-mark {
    width: 34px; height: 34px; background: var(--gloss);
  }
  .brand-name {
    font-size: 38px; letter-spacing: 2px; color: var(--gloss);
  }
  /* Back */
  .card--back { display: flex; }
  .back-brand {
    width: 210px; display: flex; flex-direction: column;
    align-items: center; justify-content: center; gap: 14px;
  }
  .back-brand .brand-mark { width: 26px; height: 26px; background: var(--silver); }
  .back-brand .brand-name { font-size: 21px; color: var(--silver); letter-spacing: 1px; }
  .pixel-band {
    width: 56px; height: 100%;
    background: linear-gradient(to bottom, #8f8f8f 0%, #3a3a3a 45%, #6e6e6e 70%, #1d1d1d 100%);
  }
  .contact {
    flex: 1; padding: 0 26px;
    display: flex; flex-direction: column; justify-content: center; gap: 14px;
    color: var(--silver); text-transform: uppercase;
  }
  .contact-name { font-size: 13px; letter-spacing: 1px; }
  .contact-phone { font-size: 12px; letter-spacing: 2px; }
  .contact-line { font-size: 8.5px; letter-spacing: .5px; color: var(--silver-soft); }
</style>
</head>
<body>
<main class="stage">
  <section class="card card--front" aria-label="Frente do cartão">
    <span class="brand-mark" aria-hidden="true"></span>
    <span class="brand-name">RTV IMOVEIS</span>
  </section>

  <section class="card card--back" aria-label="Verso do cartão">
    <div class="back-brand">
      <span class="brand-mark" aria-hidden="true"></span>
      <span class="brand-name">RTV IMOVEIS</span>
    </div>
    <div class="pixel-band" role="img" aria-label="Faixa decorativa de pequenos quadrados prateados em degradê"></div>
    <div class="contact">
      <p class="contact-name">Renata Tavares Vilela</p>
      <p class="contact-phone">41 8831 6402</p>
      <p class="contact-line">renata@rtvimoveis-exemplo.com.br</p>
      <p class="contact-line">www.RTVimoveis-exemplo.com.br</p>
    </div>
  </section>
</main>
</body>
</html>
```